VKT Logistics Marketing flyer

Good morning, I run a trucking company and I will be needing help setting up a website logo and a marketing flyer or something like that talking about our services and what we can offer to potential new customers who need to ship their product. I need help getting this all together.

Target Market(s)

Transportation customers

Requirements
Must have
• should list our services and contact info
Nice to have
• the Logo on the top

```html
<!DOCTYPE html>
<html lang="en">
<head>
<meta charset="utf-8">
<title>VKT Logistics – Services Flyer</title>
<link href="https://fonts.googleapis.com/css2?family=Anton&family=Oswald:wght@300;500;700&display=swap" rel="stylesheet">
<style>
  :root {
    --bg-dark: #151515;
    --bg-mid: #2a2a2a;
    --silver-light: #f2f2f2;
    --silver-mid: #b9b9b9;
    --silver-dark: #8a8a8a;
    --brand-blue: #1d4f91;
    --badge-red: #d60f18;
    --white: #ffffff;
    --ink: #1a1a1a;
  }
  * { margin: 0; padding: 0; box-sizing: border-box; }
  html, body { width: 927px; height: 1200px; overflow: hidden; background: var(--bg-dark); }
  .flyer {
    position: relative; width: 927px; height: 1200px; overflow: hidden;
    background: radial-gradient(ellipse at 55% 45%, var(--bg-mid) 0%, var(--bg-dark) 70%);
    font-family: "Oswald", sans-serif; color: var(--white);
  }
  .brand-name {
    position: absolute; left: 37px; top: 48px; width: 260px;
    font-family: "Oswald", sans-serif; font-weight: 700; color: var(--silver-light);
    line-height: 1;
  }
  .brand-name .brand-main { display: block; font-size: 96px; letter-spacing: 4px; }
  .brand-name .brand-sub { display: block; font-size: 27px; letter-spacing: 6px; margin-top: 6px; }
  .headline {
    position: absolute; right: 54px; top: 40px; text-align: right;
    font-family: "Anton", sans-serif; line-height: 1.22; font-size: 74px;
    background: linear-gradient(180deg, var(--silver-light) 0%, var(--silver-mid) 55%, var(--silver-light) 100%);
    -webkit-background-clip: text; background-clip: text; color: transparent;
  }
  .services {
    position: absolute; left: 31px; top: 264px; width: 865px; height: 238px;
    border: 1.5px solid var(--silver-mid); border-radius: 14px;
  }
  .services-tab {
    position: absolute; left: 308px; top: -11px; width: 249px; height: 42px;
    background: var(--brand-blue); border-radius: 4px;
    font-family: "Oswald", sans-serif; font-weight: 500; font-size: 34px; line-height: 42px;
    text-align: center; color: var(--silver-light);
  }
  .service-list { position: absolute; top: 50px; list-style: none; }
  .service-list.left { left: 28px; }
  .service-list.right { left: 431px; }
  .service-list li {
    display: flex; align-items: center; height: 30px;
    font-weight: 300; font-size: 20px; color: var(--white);
  }
  .service-list svg { width: 18px; height: 18px; margin-right: 10px; flex: none; }
  .truck-photo {
    position: absolute; left: 150px; top: 560px; width: 777px; height: 530px;
    background: radial-gradient(ellipse at 50% 55%, #b8b8b8 0%, #7d7d7d 35%, #3a3a3a 65%, transparent 80%);
  }
  .award-badge {
    position: absolute; left: 698px; top: 479px; width: 198px; height: 198px; border-radius: 50%;
    background: linear-gradient(135deg, var(--silver-light), var(--silver-dark));
  }
  .award-badge .badge-inner {
    position: absolute; left: 11px; top: 11px; width: 176px; height: 176px; border-radius: 50%;
    background: var(--badge-red); display: flex; align-items: center; justify-content: center;
  }
  .award-badge p {
    transform: rotate(-12deg); text-align: center;
    font-weight: 700; font-size: 23px; line-height: 1.18; color: var(--white);
  }
  .contact-card {
    position: absolute; left: 29px; top: 989px; width: 337px; height: 84px;
    border: 1.5px solid var(--white); border-radius: 16px 26px 22px 22px; overflow: hidden;
  }
  .contact-names {
    display: flex; height: 35px; background: var(--white); color: var(--ink);
    font-weight: 700; font-size: 17px; align-items: center;
  }
  .contact-names span, .contact-phones span { flex: 1; text-align: center; }
  .contact-phones {
    display: flex; height: 47px; align-items: center; font-weight: 700; font-size: 18px;
  }
  .contact-phones .divider { flex: none; width: 2px; height: 30px; background: var(--white); }
  .footer-band { position: absolute; left: 0; top: 1088px; width: 927px; height: 112px; }
  .footer-email {
    position: absolute; left: 34px; top: 1128px;
    font-weight: 700; font-size: 38px; color: var(--white); letter-spacing: 0.3px;
  }
  .footer-address {
    position: absolute; left: 581px; top: 1118px; color: var(--ink);
    font-weight: 300; line-height: 34px;
  }
  .footer-address .street { font-size: 24px; display: block; }
  .footer-address .web { font-size: 22px; display: block; }
</style>
</head>
<body>
<div class="flyer">
  <div class="brand-name"><span class="brand-main">VKT</span><span class="brand-sub">Logistics LLC</span></div>

  <h1 class="headline">EXCELLENCE<br>IN EVERY MILE</h1>

  <section class="services">
    <h2 class="services-tab">OUR SERVICES</h2>
    <ul class="service-list left">
      <li><svg viewBox="0 0 18 18"><rect x="1" y="4" width="12" height="12" rx="2" fill="none" stroke="#fff" stroke-width="2"/><path d="M4 9l3 3 9-10" fill="none" stroke="#fff" stroke-width="2.4"/></svg>Handling of dry van, Reefer, flatbed, or tanker loads.</li>
      <li><svg viewBox="0 0 18 18"><rect x="1" y="4" width="12" height="12" rx="2" fill="none" stroke="#fff" stroke-width="2"/><path d="M4 9l3 3 9-10" fill="none" stroke="#fff" stroke-width="2.4"/></svg>Local and cross-country transportation services.</li>
      <li><svg viewBox="0 0 18 18"><rect x="1" y="4" width="12" height="12" rx="2" fill="none" stroke="#fff" stroke-width="2"/><path d="M4 9l3 3 9-10" fill="none" stroke="#fff" stroke-width="2.4"/></svg>Solo and team drivers available.</li>
      <li><svg viewBox="0 0 18 18"><rect x="1" y="4" width="12" height="12" rx="2" fill="none" stroke="#fff" stroke-width="2"/><path d="M4 9l3 3 9-10" fill="none" stroke="#fff" stroke-width="2.4"/></svg>Pride in customer service from pick up to delivery.</li>
      <li><svg viewBox="0 0 18 18"><rect x="1" y="4" width="12" height="12" rx="2" fill="none" stroke="#fff" stroke-width="2"/><path d="M4 9l3 3 9-10" fill="none" stroke="#fff" stroke-width="2.4"/></svg>Transportation of orange juice nationally.</li>
    </ul>
    <ul class="service-list right">
      <li><svg viewBox="0 0 18 18"><rect x="1" y="4" width="12" height="12" rx="2" fill="none" stroke="#fff" stroke-width="2"/><path d="M4 9l3 3 9-10" fill="none" stroke="#fff" stroke-width="2.4"/></svg>Handling of dry van, Reefer, flatbed, or tanker loads.</li>
      <li><svg viewBox="0 0 18 18"><rect x="1" y="4" width="12" height="12" rx="2" fill="none" stroke="#fff" stroke-width="2"/><path d="M4 9l3 3 9-10" fill="none" stroke="#fff" stroke-width="2.4"/></svg>Local and cross-country transportation services.</li>
      <li><svg viewBox="0 0 18 18"><rect x="1" y="4" width="12" height="12" rx="2" fill="none" stroke="#fff" stroke-width="2"/><path d="M4 9l3 3 9-10" fill="none" stroke="#fff" stroke-width="2.4"/></svg>Solo and team drivers available.</li>
      <li><svg viewBox="0 0 18 18"><rect x="1" y="4" width="12" height="12" rx="2" fill="none" stroke="#fff" stroke-width="2"/><path d="M4 9l3 3 9-10" fill="none" stroke="#fff" stroke-width="2.4"/></svg>Pride in customer service from pick up to delivery.</li>
      <li><svg viewBox="0 0 18 18"><rect x="1" y="4" width="12" height="12" rx="2" fill="none" stroke="#fff" stroke-width="2"/><path d="M4 9l3 3 9-10" fill="none" stroke="#fff" stroke-width="2.4"/></svg>Transportation of orange juice nationally.</li>
    </ul>
  </section>

  <div class="truck-photo" role="img" aria-label="Photo of a white semi truck pulling a polished steel tanker trailer"></div>

  <div class="award-badge">
    <div class="badge-inner"><p>Winner of RMX<br>carrier excellence<br>award.</p></div>
  </div>

  <div class="contact-card">
    <div class="contact-names"><span>CEO Dana Whitfield</span><span>CEO Dana Whitfield</span></div>
    <div class="contact-phones"><span>555-204-3187</span><i class="divider"></i><span>555-316-7402</span></div>
  </div>

  <svg class="footer-band" viewBox="0 0 927 112" aria-hidden="true">
    <defs>
      <linearGradient id="footerBlue" x1="0" y1="0" x2="0" y2="1">
        <stop offset="0" stop-color="#1f5aa3"/><stop offset="1" stop-color="#163f78"/>
      </linearGradient>
      <linearGradient id="footerSilver" x1="0" y1="0" x2="1" y2="0">
        <stop offset="0" stop-color="#9a9a9a"/><stop offset="0.35" stop-color="#f4f4f4"/><stop offset="1" stop-color="#d6d6d6"/>
      </linearGradient>
    </defs>
    <polygon points="463,0 480,0 525,112 508,112" fill="#9c9c9c"/>
    <polygon points="506,18 927,18 927,112 548,112" fill="url(#footerSilver)"/>
    <polygon points="0,18 470,18 513,112 0,112" fill="url(#footerBlue)"/>
  </svg>
  <div class="footer-email">vktlogisticsllc@mailbox.com</div>
  <div class="footer-address">
    <span class="street">410 Birch Ln. Oakvale, IN. 47100</span>
    <span class="web">www.yourwebsiteaddress.com</span>
  </div>
</div>
</body>
</html>
```